Small business that sells dolls used in the investigation of sudden infant deaths needs a website de

We need a modern update to our very simple current website. We are a small business that manufactures and sells featureless dolls used in the training and investigation of sudden infant deaths. With our customer base being primarily government organizations we are looking for design that is to the point and functional while also being engaging.
Updates

Target Market(s)

Our target audience are organizations such as government offices and training organizations looking for information about our product. This makes readability and ease-of-use of the design very important.

Number of Pages Required

5+ page

Font styles to use
Serif

Colors

Designer to choose colors to be used in the design.

Requirements
Must have
• Straightforward website focused towards the product being sold. With secondary focus is being how to contact the business and the care and use of the product. The business logo is orange and blue, these colors do not necessarily need to show up in the website design. Darker and muted/contrasting colors would probably be better.
Nice to have
• It would be nice if the website had a professional feel, that is slightly maternal but is not cutesy. Given the nature of our product, we also would like a site that is very respectful for any case that our product might be used in it.

```html
<!DOCTYPE html>
<html lang="en">
<head>
<meta charset="utf-8">
<title>Gentle Hands Training Dolls – Care &amp; Usage</title>
<link rel="stylesheet" href="https://fonts.googleapis.com/css2?family=Montserrat:wght@300;400;500;600&display=swap">
<style>
  :root{
    --stage:#ececec;
    --band-dark:#3a3a3a;
    --band-dark-2:#2b2b2b;
    --tick:#3ea4ea;
    --tick-mark:#1f3342;
    --ink:#3b3b3b;
    --ink-soft:#555;
    --light-text:#d2d2d2;
    --white:#ffffff;
    --contact-bg:#f3f3f3;
    --footer:#4d4d4d;
    --footer-text:#e6e6e6;
    --alert:#f04e23;
    --doll-orange:#ff4a17;
    --icon:#4a4a4a;
  }
  *{box-sizing:border-box;margin:0;padding:0}
  html,body{width:1200px;height:1200px;overflow:hidden}
  body{background:var(--stage);font-family:"Montserrat",sans-serif;color:var(--ink)}
  .page{position:absolute;left:100px;top:0;width:1000px;height:1200px;background:var(--white);overflow:hidden}
  section,footer{position:absolute;left:0;width:1000px}
  .abs{position:absolute}

  /* Features */
  .features{top:0;height:260px;background:linear-gradient(135deg,var(--band-dark) 0%,#444 40%,var(--band-dark-2) 100%)}
  .features .backdrop{position:absolute;inset:0}
  .features h2{position:absolute;top:-6px;left:0;width:100%;text-align:center;font-weight:400;font-size:27px;color:var(--white)}
  .feature{position:absolute;top:57px;width:220px;text-align:center}
  .feature svg{display:block;margin:0 auto 22px}
  .feature p{font-size:11.5px;line-height:17px;color:var(--light-text);letter-spacing:.2px}

  /* Care */
  .care{top:260px;height:565px;background:var(--white)}
  .care h2{position:absolute;top:57px;width:100%;text-align:center;font-weight:300;font-size:27px;color:var(--ink)}
  .tip{position:absolute;top:149px;width:168px}
  .tip .photo{height:112px;border-radius:3px}
  .tip .photo.tall{height:140px}
  .tip p{margin-top:22px;font-size:9.6px;line-height:15.3px;color:var(--ink-soft);letter-spacing:.2px}
  .tip p + p{margin-top:14px}
  .tip strong{color:var(--ink);font-weight:600}
  .tip .alert{color:var(--alert);font-weight:600}
  .tip .warn{margin-top:20px;display:block}

  /* Contact */
  .contact{top:825px;height:206px;background:var(--contact-bg)}
  .contact .figure{left:170px;top:44px;width:96px;height:162px;background:var(--doll-orange);border-radius:40px 40px 10px 10px}
  .contact-item{position:absolute;display:flex;align-items:flex-start;gap:12px;font-size:11.5px;line-height:17px;color:var(--ink)}
  .contact-item.big{font-size:16.5px;line-height:20px;font-weight:300}

  /* Footer */
  .site-footer{top:1031px;height:169px;background:var(--footer);color:var(--footer-text)}
  .brand{position:absolute;left:205px;top:42px;width:160px;text-align:center;color:var(--white)}
  .brand .mark{width:42px;height:42px;border:2px solid var(--white);border-radius:50%;margin:0 auto 8px}
  .brand .name{font-weight:500;font-size:13px;line-height:13px;letter-spacing:.3px}
  .brand .tag{font-size:4.6px;margin-top:3px;text-transform:uppercase;letter-spacing:.1px}
  .nav{position:absolute;left:517px;top:40px;width:150px;list-style:none}
  .nav li,.social h3{font-size:9.3px;line-height:21px;letter-spacing:.8px;text-transform:uppercase;font-weight:400;color:var(--footer-text);white-space:nowrap}
  .social{position:absolute;left:684px;top:40px}
  .social .dots{display:flex;gap:8px;margin-top:6px}
  .social .dots span{width:13px;height:13px;border-radius:50%;background:#c9c9c9}
</style>
</head>
<body>
<main class="page">

  <section class="features">
    <div class="backdrop" role="img" aria-label="Dim background photograph of featureless training dolls on knitted fabric"></div>
    <h2>Features</h2>
    <div class="feature" style="left:150px">
      <svg width="50" height="50" viewBox="0 0 50 50"><circle cx="25" cy="25" r="25" fill="var(--tick)"/><path d="M14 26l8 8 15-16" fill="none" stroke="var(--tick-mark)" stroke-width="4" stroke-linecap="round" stroke-linejoin="round"/></svg>
      <p>The six or eight pound featureless dolls are made of light-colored fabric or orange high-visibility fabric for photographic purposes.</p>
    </div>
    <div class="feature" style="left:392px">
      <svg width="50" height="50" viewBox="0 0 50 50"><circle cx="25" cy="25" r="25" fill="var(--tick)"/><path d="M14 26l8 8 15-16" fill="none" stroke="var(--tick-mark)" stroke-width="4" stroke-linecap="round" stroke-linejoin="round"/></svg>
      <p>The orange fabric may be wiped with a germicidal solution using a damp rag.</p>
    </div>
    <div class="feature" style="left:635px">
      <svg width="50" height="50" viewBox="0 0 50 50"><circle cx="25" cy="25" r="25" fill="var(--tick)"/><path d="M14 26l8 8 15-16" fill="none" stroke="var(--tick-mark)" stroke-width="4" stroke-linecap="round" stroke-linejoin="round"/></svg>
      <p>A permanent marker may be used to mark the front and back or add facial features as desired.</p>
    </div>
  </section>

  <section class="care">
    <h2>How to use and take care of Gentle Hands Dolls</h2>

    <article class="tip" style="left:145px">
      <div class="photo" role="img" aria-label="Photo of a white fabric doll lying on a red and purple blanket" style="background:linear-gradient(135deg,#6e5a86,#a83a4a)"></div>
      <p>The dolls are made of either light colored or orange fabric so they show up well in photographs. Use a permanent marker to indicate the front and back of the doll. Add a face if desired.</p>
    </article>

    <article class="tip" style="left:326px">
      <div class="photo" role="img" aria-label="Photo of a person in red holding a white doll supported at the body" style="background:linear-gradient(90deg,#c3262a,#d63a35 55%,#4a2d22)"></div>
      <p>To help keep your doll in good shape, carry it supporting the body.</p>
    </article>

    <article class="tip" style="left:508px">
      <div class="photo" role="img" aria-label="Photo of a hand lifting a white doll by one arm against a dark background" style="background:radial-gradient(circle at 50% 60%,#d8d8d8 0,#9a9a9a 30%,#141414 60%)"></div>
      <p><span class="alert">Do not</span> carry a doll by the arm or leg as damage may occur due to the weight putting stress on the seams and fabric.</p>
      <svg class="warn" width="20" height="20" viewBox="0 0 20 20" aria-hidden="true"><rect x="3.5" y="3.5" width="13" height="13" rx="2" transform="rotate(45 10 10)" fill="var(--alert)"/><rect x="9" y="5.5" width="2" height="6" rx="1" fill="#fff"/><circle cx="10" cy="14" r="1.1" fill="#fff"/></svg>
    </article>

    <article class="tip" style="left:689px">
      <div class="photo tall" role="img" aria-label="Photo of a doll dressed in a white onesie and stocking hat marked with a letter F" style="background:radial-gradient(circle at 50% 55%,#d6d6d6 0,#8a8a8a 30%,#0d0d0d 58%)"></div>
      <p><strong>Great tip:</strong> One investigator dresses her doll in a white onesie and stocking hat. She then tucks in weights as needed. This can also help keep the dolls clean.</p>
      <p><strong>Water repellents:</strong> Some investigators have used spray-on water repellents, such as Brightline Heavy Duty Water Repellent on the dolls for protection from water and stains.</p>
    </article>
  </section>

  <section class="contact">
    <div class="abs figure" role="img" aria-label="Illustration of an orange high-visibility training doll"></div>

    <div class="contact-item" style="left:305px;top:55px">
      <svg width="26" height="28" viewBox="0 0 26 28" aria-hidden="true"><path d="M13 1C7 1 2.5 5.5 2.5 11.2 2.5 18.5 13 27 13 27s10.5-8.5 10.5-15.8C23.5 5.5 19 1 13 1z" fill="var(--icon)"/><circle cx="13" cy="11" r="3.8" fill="var(--contact-bg)"/></svg>
      <div>Gentle Hands Training Dolls,<br>218 NW Alder Lane,&nbsp; Cedar Bay,<br>WA 98000</div>
    </div>

    <div class="contact-item" style="left:305px;top:128px">
      <svg width="27" height="24" viewBox="0 0 27 24" aria-hidden="true"><path d="M1 1l25 11L1 23l4-11z" fill="var(--icon)"/><path d="M5 12h12" stroke="var(--contact-bg)" stroke-width="2"/></svg>
      <div style="padding-top:3px">contact@gentlehandsdolls.com</div>
    </div>

    <div class="contact-item big" style="left:580px;top:57px">
      <svg width="18" height="30" viewBox="0 0 18 30" aria-hidden="true"><rect x="1" y="1" width="16" height="28" rx="2" fill="var(--icon)"/><rect x="4" y="4" width="10" height="8" fill="var(--contact-bg)"/><g fill="var(--contact-bg)"><rect x="4" y="15" width="2.4" height="2.4"/><rect x="7.8" y="15" width="2.4" height="2.4"/><rect x="11.6" y="15" width="2.4" height="2.4"/><rect x="4" y="19" width="2.4" height="2.4"/><rect x="7.8" y="19" width="2.4" height="2.4"/><rect x="11.6" y="19" width="2.4" height="2.4"/><rect x="4" y="23" width="2.4" height="2.4"/><rect x="7.8" y="23" width="2.4" height="2.4"/><rect x="11.6" y="23" width="2.4" height="2.4"/></g></svg>
      <div style="padding-top:5px">(555) 014-2287</div>
    </div>

    <div class="contact-item" style="left:578px;top:125px">
      <svg width="28" height="28" viewBox="0 0 28 28" aria-hidden="true"><path d="M2 7l5-5M26 7l-5-5" stroke="var(--icon)" stroke-width="2.5" stroke-linecap="round"/><circle cx="14" cy="15" r="11" fill="var(--icon)"/><path d="M14 9v6.5l4 2.5" fill="none" stroke="var(--contact-bg)" stroke-width="2" stroke-linecap="round"/></svg>
      <div style="padding-left:2px">Monday - Friday<br>8:00 AM - 5:00 PM (Pacific Time)</div>
    </div>
  </section>

  <footer class="site-footer">
    <div class="brand">
      <div class="mark"></div>
      <div class="name">GENTLE HANDS<br>TRAINING DOLLS</div>
      <div class="tag">Training dolls for infant death investigation</div>
    </div>
    <ul class="nav">
      <li>Home</li>
      <li>About Our Dolls</li>
      <li>Care &amp; Usage</li>
      <li>Gallery</li>
      <li>About Us</li>
    </ul>
    <div class="social">
      <h3>Socialmedia</h3>
      <div class="dots"><span></span><span></span></div>
    </div>
  </footer>

</main>
</body>
</html>
```